Australia-Wide Industry Leader Bookkeeping Business Website Design Required

We need a website designed for our 10 year old bookkeeping business, Barwick & Lund. Barwick & Lund has been servicing the local & interstate communities of Australia, providing first-class BAS & Bookkeeping services with a personal touch unmatched by anyone else in the county.

What began 10 years ago as a small business focusing on family, friends and the local community, it has since grown into a well respected business with 95% of their business based solely on word of mouth and personal referrals from around Australia.

We would like to see designs that incorporate our existing brand/logo. The colours to be used on the website should be colours that work well with our logo. The design should communicate maturity, trust and confidence with a Web 2.0 look and feel.

We have produced mockups of the entire website as well as assets used in the mockups. Please reference the attached files. The mockups are an example of all the design elements that we want on each page. Designers are encouraged to use the mockups as a guideline only and for designers to use their own creativity.
Updates

This message is for new graphic designers who are considering commencing work on this project. Thank you for expressing an interest in our project. We would like to inform you that this project is close to completion as we have a number designs under very serious consideration.

We are currently in a position where we are disinterested providing feedback to improve on new designs submitted. We will provide feedback to improve new designs only if the submitted designs are very close to what we want for our website, and will only require 1 or 2 revision rounds to refine before the project completion date we will not work with designers to refine their newly submitted designs.

We feel that it is important for all designers to know the above information as we feel that your time and effort may be better spent working on another project.

Thank you for your understanding.

A big thank you for all the designs submitted. We are now in the process of selecting a design. Please be patient during this process. Thank you.

Target Market(s)

Busy Business Owners

Industry/Entity Type

Small Business

Requirements
Must have
• We require a rectangular "slide show" type feature to serve as a "teaser" to arouse the emotions of our website visitors. Each slide asks a specific question. The questions are:

- Is your paperwork in a mess?
- Do you need to get organised for the end of financial year?
- Are you sick & tired of endless amounts of paperwork & BASs?
- Do you feel frustrated & annoyed because you know your books need to be done?
- Do you lack the time & patience to get your paperwork done?
- Do you wish you had more time to do the things you enjoy doing?
- Contact Barwick & Lund today and we will transform your chaos into order.

Underneath the slide show will be a button to "Call Barwick & Lund Now - 03 5550 1827".

```html
<!DOCTYPE html>
<html lang="en">
<head>
<meta charset="utf-8">
<title>Barwick &amp; Lund — Bookkeeping</title>
<link rel="stylesheet" href="https://fonts.googleapis.com/css2?family=Sorts+Mill+Goudy&family=Lora:ital,wght@0,400;1,400;1,700&family=Roboto:wght@400&display=swap">
<style>
:root{
  --page:#f2f2f2;
  --ink:#1e1e1e;
  --muted:#6d6d6d;
  --red:#8b0a0a;
  --red-deep:#6e0000;
  --rule:#dcdcdc;
  --dots:#b9b9b9;
  --tick:#2f8a3c;
  --blue:#1e9ad6;
  --white:#ffffff;
}
*{box-sizing:border-box;margin:0;padding:0}
html,body{width:964px;height:1200px;overflow:hidden}
body{position:relative;background:var(--page);font-family:"Lora",Georgia,serif;color:var(--muted)}
.abs{position:absolute}

.brand{left:343px;top:13px;width:280px;height:48px;display:flex;align-items:center;justify-content:center;
  font-family:"Sorts Mill Goudy",serif;font-size:36px;color:var(--red);letter-spacing:.5px}

.nav{left:161px;top:86px;width:644px;height:33px;background:linear-gradient(#fff,#eeeeee);
  border-bottom:2px solid var(--red);border-radius:6px 6px 0 0;display:flex;align-items:center;padding-left:16px;gap:0}
.nav a{font-family:"Lora",serif;font-size:11px;color:#444;text-decoration:none;letter-spacing:.8px;padding:2px 8px;margin-right:8px}
.nav a.current{background:var(--red);color:var(--white);border-radius:4px}

.quote{left:161px;top:131px;width:644px;height:61px;border:1px solid var(--rule);border-radius:4px;background:#f7f7f7;
  padding:6px 18px 0 10px;font-style:italic;font-size:9.6px;line-height:16.9px;color:var(--muted)}
.quote .mark{font-family:"Sorts Mill Goudy",serif;font-size:20px;color:#555;font-style:normal;line-height:0;vertical-align:-6px;font-weight:bold}

.heading{font-family:"Sorts Mill Goudy",serif;font-size:15.5px;color:var(--ink);line-height:19.5px;padding-left:19px;position:absolute;
  border-bottom:1px solid var(--rule);padding-bottom:7px}
.heading::before{content:"";position:absolute;left:0;top:6px;width:7px;height:5px;background:var(--red)}
.heading::after{content:"";position:absolute;left:7px;top:3px;border-left:6px solid var(--red);border-top:5.5px solid transparent;border-bottom:5.5px solid transparent}

.copy{font-style:italic;font-size:9.6px;line-height:16.9px;color:var(--muted)}

.checks{list-style:none;position:absolute}
.checks li{position:relative;font-style:italic;font-size:9.4px;color:#555;height:20px;line-height:17px;padding-left:18px;border-bottom:1px dotted var(--dots)}
.checks li::before{content:"";position:absolute;left:0;top:4px;width:8px;height:8px;border:1px solid #777;background:#fff}
.checks li::after{content:"";position:absolute;left:3px;top:4px;width:3px;height:6px;border:solid var(--tick);border-width:0 2px 2px 0;transform:rotate(40deg)}
.checks li.tall{height:38px;line-height:16.9px;border-bottom:none}

.points{list-style:none;position:absolute}
.points li{position:relative;font-style:italic;font-size:9.4px;color:#555;height:20px;line-height:16px;padding-left:12px}
.points li::before{content:"";position:absolute;left:1px;top:4px;border-left:6px solid var(--blue);border-top:3.5px solid transparent;border-bottom:3.5px solid transparent}

.slide{left:534px;top:206px;width:271px;height:176px;border:1px solid var(--rule);overflow:hidden;
  background:linear-gradient(120deg,#d9d9d9 0%,#eee 35%,#e8c3c9 60%,#f0e6e3 100%)}
.slide .caption{position:absolute;left:0;right:0;bottom:0;height:44px;background:rgba(40,40,40,.78);display:flex;align-items:center;padding-left:16px;
  font-family:"Sorts Mill Goudy",serif;font-size:15px;color:var(--white)}
.slide .caption::before{content:"";border-left:8px solid var(--blue);border-top:5px solid transparent;border-bottom:5px solid transparent;margin-right:11px}

.call{left:534px;top:404px;width:271px;height:56px;overflow:hidden}
.call .top{height:28px;background:linear-gradient(#fff,#e4e4e4);font-family:"Roboto",sans-serif;font-size:18px;color:#444;line-height:30px;padding-left:42px}
.call .num{height:28px;background:var(--red);font-family:"Roboto",sans-serif;font-size:19px;color:var(--white);line-height:28px;padding-left:44px;letter-spacing:.8px}
.call .agent{position:absolute;right:0;top:-18px;width:60px;height:74px;background:linear-gradient(#e9d9c9,#dcdcdc 60%,#f4f4f4)}

.map{left:535px;top:573px;width:270px;height:208px;border:1px solid var(--rule);background:#fff;padding:8px}
.map .land{width:100%;height:100%;background:linear-gradient(160deg,#e6e6e6,#cfcfcf);border-radius:40% 30% 35% 45%/30% 35% 45% 40%}

.subhead{font-weight:700;font-style:italic;font-size:9.4px;color:#333}

.badges{left:161px;top:1047px;width:644px;height:84px}
.badge{position:absolute;top:0}

.footer{left:0;top:1153px;width:964px;height:47px;border-top:2px solid var(--red);background:linear-gradient(#fafafa,#e2e2e2)}
.footer .follow{position:absolute;left:161px;top:8px;font-style:italic;font-size:9px;color:#333;display:flex;align-items:center;gap:5px}
.social{width:10px;height:10px;border-radius:2px;display:inline-block}
.footer .legal{position:absolute;right:159px;top:8px;font-style:italic;font-size:9px;color:#333}
.footer .stamp{position:absolute;right:159px;top:25px;font-style:italic;font-size:7.5px;color:#888}
</style>
</head>
<body>

<div class="abs brand">Barwick &amp; Lund</div>

<nav class="abs nav">
  <a class="current" href="#">Home</a><a href="#">About Us</a><a href="#">Services</a><a href="#">Testimonials</a><a href="#">Articles</a><a href="#">Endorsements</a><a href="#">Links</a><a href="#">Contact Us</a>
</nav>

<blockquote class="abs quote"><span class="mark">&ldquo;</span> Lorem Ipsum is simply dummy text of the printing and typesetting industry. Lorem Ipsum has been the industry's standard dummy text ever since the 1500s, when an unknown printer took a galley of type and scrambled it to make a type specimen book. Lorem Ipsum is simply dummy text of the printing type specimen book. <span class="mark">&rdquo;</span></blockquote>

<!-- left column -->
<h2 class="heading" style="left:161px;top:208px;width:306px">Welcome to Barwick &amp; Lund</h2>
<p class="abs copy" style="left:162px;top:245px;width:322px">Lorem Ipsum is simply dummy text of the printing and typesetting industry. Lorem Ipsum has been the industry's standard dummy text ever since the 1500s, when an unknown printer took a galley of type and scrambled it to make a type specimen book.Lorem Ipsum is simply dummy text of the printing and typesetting industry. Lorem Ipsum has been the industry's standard dummy text ever since the 1500s, when an unknown printer took a galley of type and scrambled it to make a type specimen book.</p>

<h2 class="heading" style="left:161px;top:404px;width:306px">To Summarise</h2>
<ul class="checks" style="left:161px;top:441px;width:126px">
  <li>Lorem Ipsum is simply</li><li>Lorem Ipsum is simply</li><li>Lorem Ipsum is simply</li><li>Lorem Ipsum is simply</li><li>Lorem Ipsum is simply</li><li>Lorem Ipsum is simply</li>
</ul>
<ul class="checks" style="left:348px;top:441px;width:126px">
  <li>Lorem Ipsum is simply</li><li>Lorem Ipsum is simply</li><li>Lorem Ipsum is simply</li><li>Lorem Ipsum is simply</li><li>Lorem Ipsum is simply</li><li>Lorem Ipsum is simply</li>
</ul>

<h2 class="heading" style="left:161px;top:585px;width:306px">What makes Barwick &amp; Lund different<br>from other Bookkeepers</h2>
<ul class="checks" style="left:161px;top:639px;width:244px">
  <li>Lorem Ipsum is simply dummy text of the printing.</li>
  <li>Lorem Ipsum is simply.</li>
  <li>Lorem Ipsum is simply dummy text of the printing.</li>
  <li>Lorem Ipsum is simply dummy text of the printing.</li>
  <li>Lorem Ipsum is simply dummy.</li>
  <li class="tall" style="width:260px">Lorem Ipsum is simply dummy text of the printing and typesetting industry. Lorem Ipsum has been.</li>
</ul>
<ul class="points" style="left:186px;top:786px;width:240px">
  <li>Lorem Ipsum is simply</li><li>Lorem Ipsum is simply dummy text of the printing.</li><li>Lorem Ipsum is simply</li><li>Lorem Ipsum is simply dummy text.</li>
</ul>
<p class="abs copy" style="left:179px;top:872px;width:250px;color:#555">Lorem Ipsum is simply dummy text of the printing and typesetting industry.</p>
<ul class="points" style="left:186px;top:915px;width:240px">
  <li>Lorem Ipsum is simply dummy text of the.</li><li>Lorem Ipsum is simply</li><li>Lorem Ipsum is simply dummy text of the printing.</li><li>Lorem Ipsum is simply</li>
</ul>
<p class="abs subhead" style="left:179px;top:1005px">Lorem Ipsum is simply dummy text of the printing and industry.</p>

<!-- right column -->
<div class="abs slide" role="img" aria-label="Photo of a frustrated woman at a computer desk">
  <div class="caption">Is your paperwork in a mess?</div>
</div>

<div class="abs call">
  <div class="top">CALL US NOW!</div>
  <div class="num">03 5550 1827</div>
  <div class="agent" role="img" aria-label="Photo of a smiling call centre assistant with a headset"></div>
</div>

<h2 class="heading" style="left:534px;top:475px;width:306px">To Summarise</h2>
<p class="abs copy" style="left:535px;top:510px;width:272px">Lorem Ipsum is simply dummy text of the printing and typesetting industry. Lorem Ipsum has been the industry's standard dummy text ever since the 1500s.</p>

<div class="abs map"><div class="land" role="img" aria-label="Map of Australia marking service locations in major cities"></div></div>

<p class="abs subhead" style="left:534px;top:800px;color:#444">Qualifications, Memberships and Partnerships</p>
<ul class="checks" style="left:534px;top:826px;width:244px">
  <li>Lorem Ipsum is simply dummy text of the printing.</li>
  <li>Lorem Ipsum is simply.</li>
  <li>Lorem Ipsum is simply dummy text of the printing.</li>
  <li>Lorem Ipsum is simply dummy text of the printing.</li>
  <li>Lorem Ipsum is simply dummy.</li>
  <li>Lorem Ipsum is simply dummy text of the printing.</li>
  <li>Lorem Ipsum is simply dummy.</li>
</ul>

<!-- partner badges -->
<div class="abs badges">
  <svg class="badge" style="left:0" width="50" height="84" aria-hidden="true"><rect x="0.5" y="0.5" width="49" height="83" fill="#1d3c78" stroke="#777"/></svg>
  <svg class="badge" style="left:104px" width="76" height="84" aria-hidden="true"><rect x="4" y="4" width="68" height="76" rx="10" fill="#c8323a"/></svg>
  <svg class="badge" style="left:233px;top:6px" width="60" height="72" aria-hidden="true"><rect x="12" y="6" width="36" height="36" fill="#e8641e"/></svg>
  <svg class="badge" style="left:387px" width="44" height="80" aria-hidden="true"><rect x="0" y="0" width="44" height="80" fill="#111"/></svg>
  <svg class="badge" style="left:483px;top:22px" width="161" height="40" aria-hidden="true"><rect x="0" y="0" width="161" height="40" fill="#cfcfcf"/></svg>
</div>

<footer class="abs footer">
  <div class="follow">Follow Us on: <span class="social" style="background:#3b5998"></span><span class="social" style="background:#29a9e1"></span></div>
  <div class="legal">The contents of this site are copyright &copy; 2012, Barwick &amp; Lund. All Rights Reserved.</div>
  <div class="stamp">This page was last modified sat 25 Jun 2011</div>
</footer>

</body>
</html>
```